Security and Automation Company based in Texas and needs logo design also

Looking for a new logo design for our company - we are based in Texas and specialize in camera, security and home automation - We do want the main company name(Brightline Guard and Controls of Texas) with our parent company in small letters below (a Veloran Partners, LLC Company) and our License number needs to be included in the design - K74836 - Darker shades of blue preferred

Target Market(s)

We work with everyone from home to large corporate - so clean design would be helpful

Industry/Entity Type

It Company

Contact Information for Business Card

PO Box 4719
Cedar Hollow, Texas 75961
Leave a spot for the phone number and email address

Logo Text

Brightline Guard and Controls of Texas/a Veloran Partners Company/K74836

Font styles to use
Sans Serif

Colors
0255a3

```html
<!DOCTYPE html>
<html lang="en">
<head>
<meta charset="utf-8">
<title>Brightline Guard and Controls of Texas – Business Card</title>
<link rel="stylesheet" href="https://fonts.googleapis.com/css2?family=Russo+One&family=Roboto:wght@400;500;700&display=swap">
<style>
  :root {
    --brand-blue: #0255a3;
    --brand-blue-deep: #0a4f9e;
    --paper: #ffffff;
    --stage: #e9ebef;
    --ink-grey: #9a9ca1;
    --rule-grey: #b9bbbf;
    --mark-grey: #b3b5b8;
  }
  * { margin: 0; padding: 0; box-sizing: border-box; }
  html, body { width: 1200px; height: 880px; overflow: hidden; }
  body {
    background: var(--stage);
    font-family: "Roboto", Arial, sans-serif;
    position: relative;
  }
  .card {
    position: absolute;
    left: 250px;
    width: 700px;
    height: 400px;
    box-shadow: 0 6px 18px rgba(0,0,0,.18);
    overflow: hidden;
  }
  .card--front { top: 30px; background: var(--brand-blue); }
  .card--back { top: 450px; background: var(--paper); }

  .lockup {
    position: absolute;
    display: flex;
    align-items: center;
  }
  .lockup__mark {
    width: 84px; height: 84px;
    border-radius: 50%;
    flex: none;
  }
  .lockup__divider {
    width: 1px; height: 118px;
    margin: 0 22px 0 24px;
  }
  .lockup__name {
    font-family: "Russo One", "Arial Black", sans-serif;
    font-size: 27px;
    line-height: 1.05;
    letter-spacing: 1.6px;
    text-transform: uppercase;
  }
  .lockup__sub {
    font-size: 11.5px;
    margin-top: 7px;
    letter-spacing: .2px;
  }

  .card--front .lockup { left: 120px; top: 141px; color: #fff; }
  .card--front .lockup__mark { background: #fff; }
  .card--front .lockup__divider { background: rgba(255,255,255,.75); }

  .card--back .lockup { left: 46px; top: 36px; color: var(--brand-blue); }
  .card--back .lockup__mark { background: var(--mark-grey); }
  .card--back .lockup__divider { background: var(--rule-grey); }
  .card--back .lockup__sub { color: var(--ink-grey); }

  .address {
    position: absolute;
    right: 46px; top: 190px;
    text-align: right;
    color: var(--ink-grey);
    font-size: 17px;
    line-height: 1.3;
  }
  .address-rule {
    position: absolute;
    left: 290px; right: 46px; top: 245px;
    height: 1px; background: var(--rule-grey);
  }
  .person {
    position: absolute;
    left: 46px; top: 262px;
  }
  .person__name { color: var(--brand-blue); font-weight: 700; font-size: 22px; }
  .person__role { color: var(--ink-grey); font-size: 17px; margin-top: -2px; }
  .person__rule { width: 360px; height: 1px; background: var(--rule-grey); margin: 8px 0 10px; }
  .contact { list-style: none; color: var(--ink-grey); font-size: 17px; }
  .contact li { display: flex; align-items: center; gap: 10px; margin-bottom: 5px; }
  .contact svg { width: 22px; height: 22px; flex: none; }
</style>
</head>
<body>

<section class="card card--front" aria-label="Card front">
  <div class="lockup">
    <span class="lockup__mark"></span>
    <span class="lockup__divider"></span>
    <div>
      <div class="lockup__name">Brightline Guard and<br>Controls of Texas</div>
      <div class="lockup__sub">a Veloran Partners, LLC Company | License number- K74836</div>
    </div>
  </div>
</section>

<section class="card card--back" aria-label="Card back">
  <div class="lockup">
    <span class="lockup__mark"></span>
    <span class="lockup__divider"></span>
    <div>
      <div class="lockup__name">Brightline Guard and<br>Controls of Texas</div>
      <div class="lockup__sub">a Veloran Partners, LLC Company | License number- K74836</div>
    </div>
  </div>

  <address class="address" style="font-style:normal">PO Box 4719<br>Cedar Hollow, Texas 75961</address>
  <div class="address-rule"></div>

  <div class="person">
    <div class="person__name">Marcus Ellery</div>
    <div class="person__role">Project Manager</div>
    <div class="person__rule"></div>
    <ul class="contact">
      <li>
        <svg viewBox="0 0 22 22" aria-hidden="true"><circle cx="11" cy="11" r="10" fill="none" stroke="#0255a3" stroke-width="1.5"/><rect x="7.5" y="5" width="7" height="12" rx="1.2" fill="none" stroke="#0255a3" stroke-width="1.4"/><circle cx="11" cy="15" r=".8" fill="#0255a3"/></svg>
        +00(555) 210 348
      </li>
      <li>
        <svg viewBox="0 0 22 22" aria-hidden="true"><circle cx="11" cy="11" r="10" fill="none" stroke="#0255a3" stroke-width="1.5"/><rect x="5.5" y="7" width="11" height="8" fill="#0255a3"/><path d="M5.5 7 L11 11.5 L16.5 7" fill="none" stroke="#fff" stroke-width="1"/></svg>
        hello@brightlineguard.com
      </li>
    </ul>
  </div>
</section>

</body>
</html>
```